Fitness Equipment Repair Business Needs a Catchy New Business Card

We have an existing business card, however, it is quite plain and boring. We are expanding primarily in the commercial area (gyms, studios, apartment complexes etc). The business card will serve as eye candy to those managers/owners that can't be met for a face to face.
Originally I was planning for a brochure as well, but all of our information is better summarized on our website. (brasswheelservicing.ca).
I would like the card to match the colour scheme of the website and utilize the logo. It should have a professional clean feel to it, however, a little colouring outside the lines wouldn't hurt.
The example card is for my service technician (Corwin Haldane). If possible I would like to be able to edit the text to use for more than one person.

Industry/Entity Type

Appliance Repair

Contact Information for Business Card

Clean, crisp and professional but needs to be eye catching. Preferably using the black, white and red colour scheme matching the website. Double sided would be nice, but is not necessary.

Colors
ec1f27
ffffff
000000

Requirements
Must have
• Must be able to edit name, phone number and title to use for multiple people. Must show the company website (brasswheelservicing.ca).

```html
<!DOCTYPE html>
<html lang="en">
<head>
<meta charset="utf-8">
<title>Brass Wheel Servicing – Business Card</title>
<link rel="stylesheet" href="https://fonts.googleapis.com/css2?family=Open+Sans:wght@400;600;700;800&family=Marcellus+SC&display=swap">
<style>
  :root {
    --brand-red: #ec1f27;
    --ink: #000000;
    --paper: #ffffff;
    --wave-grey: #bdbdbd;
    --card-black: #0b0b0b;
    --card-black-soft: #1c1c1c;
    --bg-dark: #1a0304;
    --bg-mid: #8e1116;
  }
  * { box-sizing: border-box; margin: 0; padding: 0; }
  html, body { width: 1200px; height: 960px; overflow: hidden; }
  body {
    position: relative;
    font-family: "Open Sans", Arial, sans-serif;
    background: linear-gradient(60deg, var(--bg-dark) 0%, var(--bg-mid) 45%, var(--brand-red) 100%);
  }
  .card {
    position: absolute;
    width: 540px;
    height: 360px;
    overflow: hidden;
    background: linear-gradient(160deg, var(--card-black-soft) 0%, var(--card-black) 70%);
    box-shadow: 0 8px 22px rgba(0,0,0,.55);
  }
  .card--front { left: 53px; top: 139px; }
  .card--back  { left: 618px; top: 470px; }

  .illustration {
    position: absolute;
    background: radial-gradient(ellipse at center, #3a3a3a 0%, #161616 70%, rgba(11,11,11,0) 100%);
  }
  .brand-mark {
    position: absolute;
    color: var(--paper);
    font-family: "Open Sans", Arial, sans-serif;
    font-weight: 800;
    text-align: center;
    letter-spacing: 1px;
  }

  /* front */
  .card--front .illustration { left: 187px; top: 30px; width: 168px; height: 196px; }
  .card--front .brand-mark { left: 187px; top: 222px; width: 168px; font-size: 40px; line-height: 44px; z-index: 2; }
  .front-wave { position: absolute; left: 0; top: 0; width: 540px; height: 360px; }
  .front-url {
    position: absolute; left: 0; right: 0; top: 308px;
    text-align: center; font-size: 20px; letter-spacing: 2.4px; color: var(--ink);
  }
  .front-url strong { font-weight: 800; }

  /* back */
  .tab { position: absolute; left: 28px; width: 131px; background: var(--brand-red); }
  .tab--top { top: 0; height: 26px; }
  .tab--bottom { top: 250px; height: 29px; border-radius: 0 0 8px 8px; }
  .card--back .illustration { left: 36px; top: 56px; width: 120px; height: 138px; }
  .card--back .brand-mark { left: 36px; top: 190px; width: 120px; font-size: 30px; line-height: 34px; }
  .company-name {
    position: absolute; right: 28px; top: 22px;
    font-family: "Marcellus SC", Georgia, serif;
    font-size: 27px; font-weight: 400; color: var(--paper); letter-spacing: 1px;
  }
  .tagline {
    position: absolute; right: 28px; top: 56px;
    font-size: 12.5px; color: var(--paper); white-space: nowrap;
  }
  .person-name {
    position: absolute; right: 28px; top: 148px;
    font-size: 26px; font-weight: 700; color: var(--paper);
  }
  .person-title {
    position: absolute; right: 28px; top: 183px;
    font-size: 13px; font-weight: 600; color: var(--brand-red);
  }
  .contact-list { position: absolute; left: 239px; top: 208px; width: 275px; list-style: none; }
  .contact-item {
    height: 20px; margin-bottom: 6px; padding-right: 6px;
    background: var(--brand-red); color: var(--paper);
    text-align: right; font-size: 14.5px; line-height: 20px; white-space: nowrap;
  }
  .contact-item b { font-weight: 700; }
  .address {
    position: absolute; left: 0; right: 0; top: 320px;
    text-align: center; font-size: 12.5px; color: var(--paper); white-space: nowrap;
  }
  .address strong { font-weight: 700; }
</style>
</head>
<body>

<section class="card card--front" aria-label="Business card front">
  <div class="illustration" role="img" aria-label="Line illustration of a muscular technician in a hard hat holding a wrench"></div>
  <svg class="front-wave" viewBox="0 0 540 360" aria-hidden="true">
    <path d="M0,236 C120,230 180,278 300,282 C400,284 470,278 540,274 L540,284 C470,288 400,294 300,292 C180,288 120,244 0,248 Z" fill="var(--wave-grey)"/>
    <path d="M0,244 C120,240 180,286 300,290 C400,292 470,284 540,280 L540,360 L0,360 Z" fill="var(--brand-red)"/>
  </svg>
  <div class="brand-mark">BWS</div>
  <p class="front-url">www.<strong>brass</strong>wheel<strong>servicing</strong>.ca</p>
</section>

<section class="card card--back" aria-label="Business card back">
  <div class="tab tab--top"></div>
  <div class="illustration" role="img" aria-label="Line illustration of a muscular technician in a hard hat holding a wrench"></div>
  <div class="brand-mark">BWS</div>
  <div class="tab tab--bottom"></div>

  <h1 class="company-name">Brass Wheel Servicing</h1>
  <p class="tagline">When your machines quit mid-set, we keep them running</p>

  <h2 class="person-name">Corwin Haldane</h2>
  <p class="person-title">Service Technician</p>

  <ul class="contact-list">
    <li class="contact-item"><b>Personal:</b> 555-014-2286</li>
    <li class="contact-item"><b>Service Line:</b> 555-017-3390</li>
    <li class="contact-item"><b>Service Email:</b> bwsrepair@mail.ca</li>
  </ul>

  <p class="address">1175 Corbel Road NW • Riverton • AB T0K 4P2 / <strong>www.brasswheelservicing.ca</strong></p>
</section>

</body>
</html>
```